Our company TrulaPay, an online processor of payments is seeking talented submissions for our website redesign. The winning design will be chopped up and converted into a WordPress theme to allow for easy content additions and updates.

We are looking for modern designs that rival current websites in our industry (plimo.example, zanquetto.example, holvix.example, brandle.example, quillmarkcharges.example, evensplitcharges.example, KoboRun.example).

Our company is seeking to expand our reach to software developers and engineers who are either integrating our payment platform into their offerings or are engineering a custom solution for the company they work for and are in need of a payment platform such as our own.

We currently work with hundreds of different business partners whom either resell our services or integrate our processing capabilities into their software (which they sell). We also must communicate effectively to end users, businesses, who seek us out directly for their payment processing needs.

We are open to different color schemes but would ultimately like them to be somewhat inline with our current logo (see attached). Our website needs to instill security and confidence to any current and/or potential user as we are trusted with private and sensitive information.

We are seeking submissions from qualified; individual freelancers, freelance teams, and agencies who can attack this project in its entirety. Since this project is a total redesign, we would like submissions that have the capability to design any custom graphics, icons, buttons, and illustrations in line with our industry, capabilities, offerings, and content. We are looking for someone to design our new website and would prefer a vendor who can also help us to design elements (graphics, illustrations, charts, workflows) within our website.

Designs will be converted into a wordpress theme and we would like to utilize widgets for as many areas as possible to make editing and updating easy.

We are seeking the creation of a few unique pages but many of the pages for the majority of our content will just be internal content pages which will be duplicated.

We will likely contract with the winning submission for future work.

Please see Design Reference Document for more information

Target Market(s)

Resellers
Merchant Service Providers
Software Developers
Independent Sales Organizations (ISOs)
App Builders
Mobile App Builders
Independent Software Developers
Organizational Software Developers
Businesses who need to accept payments
Governments
Municipalities
Schools
DMVs
Courts
Retailers
Medical Offices
Hosipitals
Clinics
Dr. Offices
Gyms
Churches
Non-Profits
Software Companies
Technology Companies
Startups

• Logo cannot change drastically.

```html
<!DOCTYPE html>
<html lang="en">
<head>
<meta charset="utf-8">
<title>TrulaPay – Accept payments in your app or website</title>
<link href="https://fonts.googleapis.com/css2?family=Raleway:wght@300;400;500&family=Open+Sans:wght@400;600&family=Oswald:wght@400&display=swap" rel="stylesheet">
<style>
:root{
  --red:#e20a0f;
  --navy:#22226e;
  --ink:#333;
  --muted:#666;
  --pale:#aaa;
  --line:#e3e3e3;
  --foot:#f2f2f2;
  --white:#fff;
}
*{margin:0;padding:0;box-sizing:border-box}
html,body{width:683px;height:1200px;overflow:hidden;background:var(--white)}
body{position:relative;font-family:"Open Sans",sans-serif;color:var(--ink)}
.abs{position:absolute}

/* header */
.site-header{position:absolute;left:0;top:0;width:683px;height:51px;background:var(--white)}
.brand{left:105px;top:14px;font-family:"Raleway",sans-serif;font-weight:500;font-size:19px;color:var(--navy);display:flex;align-items:center;gap:5px}
.brand-dot{width:8px;height:8px;background:var(--red);border-radius:50%}
.nav{top:22px;font-family:"Raleway",sans-serif;font-size:8px;color:#555}
.nav-more{color:var(--navy)}
.phone{left:472px;top:21px;font-family:"Open Sans",sans-serif;font-weight:600;font-size:8.5px;color:#333;display:flex;align-items:center;gap:5px}
.login{left:543px;top:21px;width:37px;height:14px;border:1px solid #bbb;border-radius:8px;font-size:6.5px;text-align:center;line-height:12px;color:#555}

/* hero */
.hero{left:0;top:51px;width:683px;height:214px;background:radial-gradient(ellipse at 50% 80%,#6a5a3a 0%,#2a2a2c 35%,#151517 100%)}
.hero-title{left:0;top:64px;width:683px;text-align:center;font-family:"Raleway",sans-serif;font-weight:300;color:var(--white);line-height:29px}
.hero-title .l1{font-size:25px}
.hero-title .l2{font-size:23px;font-weight:400}
.hero-arrow{left:307px;top:127px}

/* audience band */
.band{left:0;top:265px;width:683px;height:45px;background:var(--red)}
.band-divider{left:345px;top:274px;width:1px;height:27px;background:rgba(255,255,255,.5)}
.band-link{top:274px;display:flex;align-items:center;gap:10px;font-family:"Oswald",sans-serif;font-size:20px;color:var(--white);letter-spacing:.2px}
.band-icon{width:34px;height:34px;border-radius:50%;background:var(--white);display:flex;align-items:center;justify-content:center}

/* welcome */
.welcome-title{left:102px;top:330px;font-family:"Raleway",sans-serif;font-weight:300;font-size:21px;color:#444}
.welcome-copy{left:102px;width:464px;font-size:6.6px;line-height:11.6px;color:var(--muted)}

/* industries */
.industry-photo{left:0;top:462px;width:351px;height:190px;background:linear-gradient(110deg,#9fb7c4 0%,#d9c9b6 45%,#efe6da 100%)}
.industry-panel{left:351px;top:462px;width:332px;height:190px;background:var(--navy)}
.industry-notch{left:344px;top:624px;width:0;height:0;border-top:7px solid transparent;border-bottom:7px solid transparent;border-right:7px solid var(--navy)}
.industry-title{left:373px;top:473px;font-family:"Raleway",sans-serif;font-size:15px;color:var(--white)}
.industry-list{left:380px;top:502px;list-style:none;font-size:8.6px;color:var(--white)}
.industry-list li{height:19.5px;display:flex;align-items:center;gap:8px}
.industry-list svg{width:10px;height:10px}

/* diagram */
.diagram-title{left:0;top:679px;width:683px;text-align:center;font-family:"Raleway",sans-serif;font-size:19.5px;color:#444}
.rule{top:692px;height:1px;background:var(--line)}
.card{top:733px;width:155px;height:214px;background:var(--white);box-shadow:0 1px 3px rgba(0,0,0,.15)}
.card-top{position:absolute;left:0;top:0;width:100%;height:3px}
.card-flag{position:absolute;left:8px;top:3px;width:0;height:0;border-left:5px solid transparent;border-right:5px solid transparent}
.avatar{position:absolute;left:46px;top:22px;width:64px;height:64px;border-radius:50%}
.role{position:absolute;left:0;top:103px;width:100%;text-align:center;font-family:"Raleway",sans-serif;font-size:14px}
.chev{position:absolute;left:58px;top:126px}
.bank{position:absolute;left:62px;top:150px}
.bank-label{position:absolute;left:0;top:189px;width:100%;text-align:center;font-family:"Raleway",sans-serif;font-size:8.5px;color:var(--pale)}
.flow-icons{position:absolute;left:0;top:16px;width:100%;display:flex;justify-content:space-around;padding:0 8px}
.flow-sep{position:absolute;left:0;top:57px;width:100%;height:1px;background:var(--line)}
.flow-item{position:absolute;left:18px;display:flex;align-items:center;gap:10px;font-family:"Raleway",sans-serif;font-size:8.5px;color:var(--pale);line-height:11px}

/* features */
.feature{top:1000px;width:140px}
.feature-icon{position:absolute;left:0;top:0;width:36px;height:36px;border-radius:50%;background:var(--white);box-shadow:0 1px 3px rgba(0,0,0,.18);display:flex;align-items:center;justify-content:center}
.feature-title{position:absolute;left:45px;top:2px;font-family:"Raleway",sans-serif;font-size:13.5px;line-height:15.5px;color:#444;white-space:nowrap}
.feature-copy{position:absolute;left:6px;top:46px;font-size:6.6px;line-height:11.6px;color:var(--muted)}

/* footer */
.site-footer{left:0;top:1114px;width:683px;height:74px;background:var(--foot)}
.foot-title{top:1128px;font-family:"Raleway",sans-serif;font-size:11.5px;color:#555}
.foot-list{top:1148px;list-style:none;font-size:6.6px;color:#555;line-height:11.6px}
.foot-list li::before{content:"›";font-weight:600;margin-right:6px;font-size:8px}
.social{top:1130px;width:14px;height:14px;border-radius:50%}
.copyright{left:500px;top:1148px;width:73px;text-align:right;font-size:6.6px;line-height:11.6px;color:#555}
</style>
</head>
<body>

<header class="site-header">
  <div class="abs brand"><span>TrulaPay</span><span class="brand-dot"></span></div>
  <nav>
    <span class="abs nav" style="left:214px">Home</span>
    <span class="abs nav" style="left:253px">Solutions</span>
    <span class="abs nav" style="left:303px">Developers</span>
    <span class="abs nav" style="left:359px">Partners</span>
    <span class="abs nav nav-more" style="left:402px">More <svg width="6" height="4" style="margin-left:6px"><path d="M0 0h6L3 4z" fill="#555"/></svg></span>
  </nav>
  <div class="abs phone"><svg width="9" height="9" viewBox="0 0 24 24"><path fill="#e20a0f" d="M6.6 10.8c1.4 2.8 3.8 5.1 6.6 6.6l2.2-2.2c.3-.3.7-.4 1-.2 1.1.4 2.3.6 3.6.6.6 0 1 .4 1 1V20c0 .6-.4 1-1 1C10.6 21 3 13.4 3 4c0-.6.4-1 1-1h3.5c.6 0 1 .4 1 1 0 1.3.2 2.5.6 3.6.1.3 0 .7-.2 1z"/></svg>555 013 2847</div>
  <div class="abs login">Login</div>
</header>

<section>
  <div class="abs hero" role="img" aria-label="Businessman in a dark suit holding a glowing light bulb between open hands"></div>
  <h1 class="abs hero-title"><span class="l1">Accept payments</span><br><span class="l2">in your app or website</span></h1>
  <svg class="abs hero-arrow" width="44" height="44" viewBox="0 0 44 44">
    <circle cx="22" cy="22" r="21" fill="none" stroke="rgba(255,255,255,.25)" stroke-width="2"/>
    <circle cx="22" cy="22" r="18" fill="#e20a0f"/>
    <path d="M22 13v16M15 22l7 7 7-7" fill="none" stroke="#fff" stroke-width="3" stroke-linecap="round" stroke-linejoin="round"/>
  </svg>
</section>

<section>
  <div class="abs band"></div>
  <a class="abs band-link" style="left:115px">
    <span class="band-icon"><svg width="16" height="18" viewBox="0 0 16 18"><circle cx="8" cy="5" r="4" fill="#22226e"/><path d="M0 18c0-5 3.5-8 8-8s8 3 8 8z" fill="#22226e"/><path d="M8 10l1 3-1 4-1-4z" fill="#e20a0f"/></svg></span>
    BUSINESSES CLICK HERE
  </a>
  <div class="abs band-divider"></div>
  <a class="abs band-link" style="left:380px">
    <span class="band-icon"><svg width="16" height="18" viewBox="0 0 16 18"><circle cx="8" cy="5" r="4" fill="#22226e"/><path d="M0 18c0-5 3.5-8 8-8s8 3 8 8z" fill="#22226e"/><path d="M8 10l1 3-1 4-1-4z" fill="#e20a0f"/></svg></span>
    DEVS CLICK HERE
  </a>
</section>

<section>
  <h2 class="abs welcome-title">Welcome...</h2>
  <p class="abs welcome-copy" style="top:362px">Lorem ipsum dolor sit amet, consectetur adipiscing elit. Donec luctus sodales faucibus. Integer in augue a metus vehicula laoreet nec ac sem. Praesent ullamcorper purus a tortor tempus, suscipit consequat tortor rhoncus. In porttitor hendrerit massa, sit amet auctor ipsum elementum ut. Pellentesque sit amet volutpat est. Sed magna dolor, mollis non nisl eget, molestie vehicula magna. Fusce sed rhoncus erat.</p>
  <p class="abs welcome-copy" style="top:409px">Lorem ipsum dolor sit amet, consectetur adipiscing elit. Donec luctus sodales faucibus. Integer in augue a metus vehicula laoreet nec ac sem. Praesent ullamcorper purus a tortor tempus, suscipit consequat tortor rhoncus.</p>
</section>

<section>
  <div class="abs industry-photo" role="img" aria-label="Woman at a laptop holding a payment card"></div>
  <div class="abs industry-panel"></div>
  <div class="abs industry-notch"></div>
  <h3 class="abs industry-title">Custom Industry Solutions</h3>
  <ul class="abs industry-list">
    <li><svg viewBox="0 0 10 10"><path d="M0 10V5h2v5zM3 10V3h2v7zM6 10V4h2v6zM9 10V1h1v9z" fill="#fff"/></svg>Custom Industry Solutions</li>
    <li><svg viewBox="0 0 10 10"><path d="M5 0l5 2.5H0zM1 3h1v5H1zM4 3h2v5H4zM8 3h1v5H8zM0 8.5h10V10H0z" fill="#fff"/></svg>Government</li>
    <li><svg viewBox="0 0 10 10"><path d="M5 9.5L1 5.5A2.4 2.4 0 015 2a2.4 2.4 0 014 3.5z" fill="#fff"/><path d="M2 5h2l1-1.5L6 6l1-1h1" stroke="#22226e" stroke-width=".8" fill="none"/></svg>Medical</li>
    <li><svg viewBox="0 0 10 10"><path d="M0 4h2v2H0zM8 4h2v2H8zM2 2.5h1.5v5H2zM6.5 2.5H8v5H6.5zM3.5 4.5h3v1h-3z" fill="#fff"/></svg>Fitness</li>
    <li><svg viewBox="0 0 10 10"><circle cx="7" cy="1.5" r="1.3" fill="#fff"/><path d="M1 2l5 2 1 2-2 4H4l1.5-3.5L0 3z" fill="#fff"/></svg>Martial Arts</li>
    <li><svg viewBox="0 0 10 10"><circle cx="5" cy="5" r="4" fill="none" stroke="#fff" stroke-width="1.3"/><path d="M5 2.5V5h2" stroke="#fff" stroke-width="1.1" fill="none"/></svg>Alarm Monitoring</li>
    <li><svg viewBox="0 0 10 10"><path d="M5 0.5L10 5H8.5v4.5H6V6.5H4v3H1.5V5H0z" fill="#fff"/></svg>Property Management</li>
  </ul>
</section>

<section>
  <div class="abs rule" style="left:95px;width:87px"></div>
  <h2 class="abs diagram-title">Electronic Check Process Diagram</h2>
  <div class="abs rule" style="left:502px;width:85px"></div>

  <div class="abs card" style="left:95px">
    <div class="card-top" style="background:var(--navy)"></div>
    <div class="card-flag" style="border-top:5px solid var(--navy)"></div>
    <div class="avatar" role="img" aria-label="Buyer figure" style="background:radial-gradient(circle at 50% 40%,#3a3a8a 0%,#22226e 55%,#ededed 56%)"></div>
    <div class="role" style="color:var(--navy)">BUYER</div>
    <svg class="chev" width="40" height="14"><path d="M0 0l20 12L40 0" fill="none" stroke="#ddd" stroke-width="4"/></svg>
    <svg class="bank" width="32" height="30" viewBox="0 0 32 30"><path d="M16 0l16 7H0z" fill="#22226e"/><path d="M0 8h32v2H0zM3 12h3.5v12H3zM10 12h3.5v12H10zM18.5 12H22v12h-3.5zM25.5 12H29v12h-3.5zM0 25h32v2H0zM-0 28h32v2H0z" fill="#22226e"/></svg>
    <div class="bank-label">BUYER'S BANK (RDFI)</div>
  </div>

  <div class="abs card" style="left:262px">
    <div class="card-top" style="background:#444"></div>
    <div class="card-flag" style="border-top:5px solid #444"></div>
    <div class="flow-icons">
      <svg width="28" height="28" viewBox="0 0 28 28"><rect x="1" y="2" width="26" height="17" rx="1.5" fill="none" stroke="#555" stroke-width="2.5"/><path d="M12 19h4v4h-4zM7 24h14v2H7z" fill="#555"/></svg>
      <svg width="16" height="28" viewBox="0 0 16 28"><rect x="1" y="3" width="14" height="24" rx="2" fill="#555"/><rect x="3" y="6" width="10" height="7" fill="#fff"/><path d="M3 1h2v3H3z" fill="#555"/><g fill="#fff"><rect x="3" y="15" width="2.5" height="2"/><rect x="6.8" y="15" width="2.5" height="2"/><rect x="10.5" y="15" width="2.5" height="2"/><rect x="3" y="19" width="2.5" height="2"/><rect x="6.8" y="19" width="2.5" height="2"/><rect x="10.5" y="19" width="2.5" height="2"/></g></svg>
      <svg width="30" height="28" viewBox="0 0 30 28"><path d="M0 4h26v18H0z" fill="#555"/><path d="M0 4l13 10L26 4" fill="none" stroke="#fff" stroke-width="1.8"/><path d="M17 24l10-12 3 2.5-10 12-4 1z" fill="#555" stroke="#fff" stroke-width="1"/></svg>
    </div>
    <div class="flow-sep"></div>
    <div class="flow-item" style="top:80px"><svg width="26" height="26" viewBox="0 0 26 26"><rect width="26" height="26" rx="3" fill="#ccc"/><rect x="7" y="7" width="12" height="12" fill="#fff"/><rect x="10" y="10" width="6" height="6" fill="#ccc"/></svg>ZANQUETTO.EXAMPLE</div>
    <div class="flow-item" style="top:120px"><svg width="28" height="26" viewBox="0 0 32 30"><path d="M16 0l16 7H0z" fill="#bbb"/><path d="M0 8h32v2H0zM3 12h3.5v12H3zM10 12h3.5v12H10zM18.5 12H22v12h-3.5zM25.5 12H29v12h-3.5zM0 25h32v3H0z" fill="#bbb"/></svg><span>ZANQUETTO.EXAMPLE<br>BANK (OFDI)</span></div>
    <div class="flow-item" style="top:168px"><svg width="28" height="20" viewBox="0 0 28 20"><rect x="10" y="0" width="8" height="6" fill="#bbb"/><path d="M14 6v4M4 10h20M4 10v4M14 10v4M24 10v4" stroke="#bbb" stroke-width="1.5"/><rect x="0" y="14" width="8" height="6" fill="#bbb"/><rect x="10" y="14" width="8" height="6" fill="#bbb"/><rect x="20" y="14" width="8" height="6" fill="#bbb"/></svg>ACH NETWORK</div>
  </div>

  <div class="abs card" style="left:430px">
    <div class="card-top" style="background:var(--red)"></div>
    <div class="card-flag" style="border-top:5px solid var(--red)"></div>
    <div class="avatar" role="img" aria-label="Seller figure" style="background:radial-gradient(circle at 50% 40%,#f02a2f 0%,#e20a0f 55%,#ededed 56%)"></div>
    <div class="role" style="color:var(--red)">SELLER</div>
    <svg class="chev" width="40" height="14"><path d="M0 0l20 12L40 0" fill="none" stroke="#ddd" stroke-width="4"/></svg>
    <svg class="bank" width="32" height="30" viewBox="0 0 32 30"><path d="M16 0l16 7H0z" fill="#e20a0f"/><path d="M0 8h32v2H0zM3 12h3.5v12H3zM10 12h3.5v12H10zM18.5 12H22v12h-3.5zM25.5 12H29v12h-3.5zM0 25h32v2H0zM0 28h32v2H0z" fill="#e20a0f"/></svg>
    <div class="bank-label">SELLER'S BANK ACCOUNT</div>
  </div>
</section>

<section>
  <div class="abs feature" style="left:102px">
    <div class="feature-icon"><svg width="18" height="18" viewBox="0 0 18 18"><rect x="2" y="6" width="14" height="11" rx="2" fill="#e20a0f"/><path d="M6 6V4a3 3 0 016 0v2" fill="none" stroke="#e20a0f" stroke-width="1.8"/><circle cx="9" cy="11.5" r="2" fill="#fff"/></svg></div>
    <h4 class="feature-title">Payment<br>Gateway</h4>
    <p class="feature-copy" style="width:130px">Lorem ipsum dolor sit amet, consectetur adipiscing elit. Donec luctus sodales faucibus.</p>
  </div>
  <div class="abs feature" style="left:246px">
    <div class="feature-icon"><svg width="18" height="16" viewBox="0 0 18 16"><rect x="4" y="0" width="14" height="10" rx="1.5" fill="#e20a0f" opacity=".6"/><rect x="0" y="5" width="14" height="10" rx="1.5" fill="#e20a0f"/><rect x="0" y="7.5" width="14" height="2" fill="#fff"/></svg></div>
    <h4 class="feature-title">Ach<br>Payment API</h4>
    <p class="feature-copy" style="width:130px">Lorem ipsum dolor sit amet, consectetur adipiscing elit. Donec luctus sodales faucibus.</p>
  </div>
  <div class="abs feature" style="left:388px">
    <div class="feature-icon"><svg width="20" height="16" viewBox="0 0 20 16"><rect x="0" y="3" width="17" height="12" rx="1.5" fill="none" stroke="#e20a0f" stroke-width="1.6"/><path d="M3 11h6M3 8h3" stroke="#e20a0f" stroke-width="1.4"/><path d="M10 10l8-8 2 2-8 8-3 1z" fill="#e20a0f"/></svg></div>
    <h4 class="feature-title">Processing for Software<br>Development</h4>
    <p class="feature-copy" style="width:190px">Lorem ipsum dolor sit amet, consectetur adipiscing elit. Donec luctus sodales faucibus.&nbsp; Lorem ipsum dolor sit amet, consectetur adipiscing elit.</p>
  </div>
</section>

<footer>
  <div class="abs site-footer"></div>
  <h5 class="abs foot-title" style="left:108px">Contact Information</h5>
  <ul class="abs foot-list" style="left:108px">
    <li>Call us at : 555 013 2847</li>
    <li>Email us at : info@trulapay.example</li>
  </ul>
  <h5 class="abs foot-title" style="left:254px">Accept Credit Cards</h5>
  <ul class="abs foot-list" style="left:254px">
    <li>Online Invoicing</li>
    <li>Payment Buttons</li>
  </ul>
  <span class="abs social" style="left:523px;background:#3b5a9a"></span>
  <span class="abs social" style="left:541px;background:#2aa3dc"></span>
  <span class="abs social" style="left:559px;background:#1b7bb5"></span>
  <p class="abs copyright">Copyright © 2014<br>All Rights Reserved</p>
</footer>

</body>
</html>
```